Mrs Pellow's Menu Design

Our website is MrsPellows.com.au
Please take inspiration in the look and feel, style and tone from the photos of our takeaway restaurant.

We' have been providing our famous Chinese take away in Merrylands for over 30 years. We have seen the neighbourhood grow around us and we have grown along with them.
We have had a recent shopfitting (see photos on http://www.mrspellows.com.au).

Red features prominently in our shop design but understand if you would keep it muted or minimal for readability.

We would like to revamp our plain menu to a fresh new look with a typeface that emphasizes familiarity and simple, delicious food.
Updates

Reason: Updated brief with more information Would like more designs

Target Market(s)

Our customers are locals who have enjoyed our famous Chinese takeaway for over 30 years. They are mums buying takeout for their family dinner, staff from the surrounding mall shops after a quick, delicious feed and regulars who come in every week for their fix of freshly prepared, familiar Chinese favourites like san choy bow, crispy salt and pepper squid and stir-fried beef in black bean sauce.

Industry/Entity Type

Shop

Requirements
Must have
• Typeface is very important.
It must be readable and convey a classic Chinese menu that oozes familiarity and sincerity. We serve simple, classic Chinese favorites at a economical price
Should not have
• Should not be childish, cartoony or cliched.

```html
<!DOCTYPE html>
<html lang="en">
<head>
<meta charset="utf-8">
<title>Mrs. Pellow's Menu</title>
<link href="https://fonts.googleapis.com/css2?family=Arimo:wght@400;700&family=Gelasio:wght@700&display=swap" rel="stylesheet">
<style>
  :root {
    --frame: #3d6fd6;
    --frame-light: #6f9cf0;
    --wood-dark: #4e3112;
    --wood-mid: #6b4719;
    --wood-light: #80592a;
    --text: #ffffff;
    --text-soft: #f3efe6;
    --art: #2b3fae;
    --band: #3a2a16;
  }
  * { margin: 0; padding: 0; box-sizing: border-box; }
  html, body { width: 1200px; height: 900px; overflow: hidden; background: var(--frame); }
  .menu {
    position: relative;
    width: 1200px; height: 900px;
    border: 6px solid var(--frame);
    outline: 1px solid var(--frame-light);
    outline-offset: -7px;
    background:
      linear-gradient(100deg, rgba(0,0,0,.18), rgba(255,255,255,.04) 40%, rgba(0,0,0,.12) 70%, rgba(255,255,255,.05)),
      linear-gradient(180deg, var(--wood-mid), var(--wood-light) 45%, var(--wood-dark));
    font-family: "Arimo", Arial, sans-serif;
    color: var(--text);
    font-size: 13px;
  }
  .centre-art {
    position: absolute;
    left: 470px; top: 140px; width: 280px; height: 460px;
    border-radius: 140px 140px 60px 60px;
    background: radial-gradient(ellipse at center, rgba(43,63,174,.35), rgba(43,63,174,.08) 70%, transparent);
  }
  .column { position: absolute; top: 0; }
  .column--left { left: 2px; width: 328px; }
  .column--middle { left: 418px; width: 356px; }
  .column--right { left: 834px; width: 356px; }
  .section { position: absolute; left: 0; right: 0; }
  .section-title {
    font-family: "Gelasio", "Palatino Linotype", serif;
    font-weight: 700;
    font-size: 21px;
    line-height: 24px;
    color: var(--text);
  }
  .column--right .section-title { line-height: 22px; }
  .item {
    display: flex;
    align-items: baseline;
    white-space: nowrap;
    line-height: 18.3px;
  }
  .column--right .item { line-height: 16.6px; }
  .item .name { flex: none; }
  .item .note { font-size: 9px; }
  .item .leader {
    flex: 1;
    border-bottom: 1.5px dotted var(--text-soft);
    margin: 0 3px;
    transform: translateY(-3px);
    min-width: 6px;
  }
  .item .price { flex: none; }
  .item--sub { padding-left: 12px; }
  .item--tight { line-height: 15px; }
  .item--sub-note { padding-left: 8px; font-size: 9px; }
  .item--sub-note .price { font-size: 13px; }
  .footer-rule {
    position: absolute; left: 0; right: 0; top: 865px;
    border-top: 2px solid var(--text);
  }
  .footer {
    position: absolute; left: 0; right: 0; top: 869px; height: 25px;
    background: linear-gradient(180deg, rgba(40,28,14,.6), var(--band));
    text-align: center;
    font-weight: 700;
    font-size: 13px;
    line-height: 24px;
  }
</style>
</head>
<body>
<div class="menu">
  <div class="centre-art" role="img" aria-label="Decorative line illustration of a Chinese guardian lion figure in blue"></div>

  <div class="column column--left">
    <section class="section" style="top:8px">
      <h2 class="section-title">Mrs. Pellow's Specials</h2>
      <div class="item item--tight" style="line-height:18.3px"><span class="name">Golden Fried Box</span></div>
      <div class="item item--sub"><span class="name">Regular <span class="note">(1 Spring Roll, 1 Curry Meat Pastry, 2 Dim Sims, 1 Prawn Cutlet)</span></span><span class="price">&nbsp;$6.50</span></div>
      <div class="item item--sub" style="line-height:16px"><span class="name">Large <span class="note">(1 Spring Roll, 1 Curry Meat Pastry, 4 Dim Sims, 2 Prawn Cutlets)</span></span><span class="leader"></span><span class="price">$9.50</span></div>
      <div class="item" style="line-height:16px"><span class="name">Seafood Combination with Oyster Sauce</span></div>
      <div class="item item--sub-note" style="line-height:16px"><span class="name">(King Prawn, Scallop, Calamari, Mushrooms &amp; Babycorn)</span><span class="leader"></span><span class="price">$12.00</span></div>
      <div class="item"><span class="name">Sate Combination <span class="note">(Beef, Chicken &amp; King Prawn)</span></span><span class="leader"></span><span class="price">$11.00</span></div>
      <div class="item"><span class="name">Garlic &amp; Chilli Combination <span class="note">(Beef, Chicken &amp; King Prawn)</span></span><span class="leader"></span><span class="price">$11.00</span></div>
      <div class="item"><span class="name">Combination in Oyster Sauce <span class="note">(Beef, Chicken &amp; King Prawn)</span></span><span class="price">&nbsp;$11.00</span></div>
      <div class="item"><span class="name">Mongolian Lamb Fillet</span><span class="leader"></span><span class="price">$10.80</span></div>
      <div class="item"><span class="name">Deep Fried Lamb Fillet with Special Sauce</span><span class="leader"></span><span class="price">$10.80</span></div>
      <div class="item"><span class="name">Braised Chicken with Szechuan Sauce (Hot)</span><span class="leader"></span><span class="price">$9.90</span></div>
      <div class="item"><span class="name">Braised Chicken with Sweet Chilli Sauce</span><span class="leader"></span><span class="price">$9.90</span></div>
      <div class="item"><span class="name">Salt &amp; Pepper Squid</span><span class="leader"></span><span class="price">$10.00</span></div>
      <div class="item"><span class="name">Singapore Fried Noodles</span><span class="leader"></span><span class="price">$8.50</span></div>
    </section>

    <section class="section" style="top:306px">
      <h2 class="section-title">Entreé</h2>
      <div class="item"><span class="name">Mini Spring Rolls (6)</span><span class="leader"></span><span class="price">$5.50</span></div>
      <div class="item"><span class="name">Spring Roll</span><span class="leader"></span><span class="price">$1.50</span></div>
      <div class="item"><span class="name">Curried Meat Pastry</span><span class="leader"></span><span class="price">$1.50</span></div>
      <div class="item"><span class="name">Dim Sim (Deep Fried)</span><span class="leader"></span><span class="price">$1.00</span></div>
      <div class="item"><span class="name">Dim Sims (Steamed) (6)</span><span class="leader"></span><span class="price">$5.50</span></div>
      <div class="item"><span class="name">Prawn Cutlet</span><span class="leader"></span><span class="price">(each)&nbsp; $1.70 ..... (6)&nbsp; $9.90</span></div>
      <div class="item"><span class="name">Chicken Wings (Deep Fried)</span><span class="leader"></span><span class="price">$5.50</span></div>
    </section>

    <section class="section" style="top:483px">
      <h2 class="section-title">Soup</h2>
      <div class="item"><span class="name">Hot &amp; Sour Soup</span><span class="leader" style="flex:0 0 60px"></span><span class="price" style="flex:1;text-align:right">Small&nbsp; $4.80 ... Large&nbsp; $6.80</span></div>
      <div class="item"><span class="name">Short Soup</span><span class="leader"></span><span class="price">$4.00</span></div>
      <div class="item"><span class="name">Long Soup</span><span class="leader"></span><span class="price">$4.00</span></div>
      <div class="item"><span class="name">Combination Soup</span><span class="leader"></span><span class="price">$4.00</span></div>
      <div class="item"><span class="name">Combination Long Soup</span><span class="leader"></span><span class="price">$7.00</span></div>
      <div class="item"><span class="name">Combination Short Soup</span><span class="leader"></span><span class="price">$7.00</span></div>
      <div class="item"><span class="name">Mixed Short &amp; Long Soup</span><span class="leader"></span><span class="price">$7.00</span></div>
      <div class="item"><span class="name">Sweet Corn Crab Meat Soup</span><span class="leader"></span><span class="price">$4.50</span></div>
      <div class="item"><span class="name">Chicken Sweet Corn Soup</span><span class="leader"></span><span class="price">$4.50</span></div>
    </section>

    <section class="section" style="top:697px">
      <h2 class="section-title">Sweet &amp; Sour</h2>
      <div class="item"><span class="name">Sweet &amp; Sour Pork</span><span class="leader"></span><span class="price">$8.80</span></div>
      <div class="item"><span class="name">Sweet &amp; Sour Beef</span><span class="leader"></span><span class="price">$9.90</span></div>
      <div class="item"><span class="name">Sweet &amp; Sour Braised Chicken</span><span class="leader"></span><span class="price">$9.90</span></div>
      <div class="item"><span class="name">Sweet &amp; Sour Chicken Fritters</span><span class="leader"></span><span class="price">$9.90</span></div>
      <div class="item"><span class="name">Sweet &amp; Sour Combination <span class="note">(Beef, Chicken &amp; King Prawn)</span></span><span class="leader"></span><span class="price">$11.00</span></div>
      <div class="item"><span class="name">Sweet &amp; Sour King Prawns Fritters</span><span class="leader"></span><span class="price">$11.50</span></div>
    </section>
  </div>

  <div class="column column--middle">
    <section class="section" style="top:8px">
      <h2 class="section-title">King Prawns</h2>
      <div class="item"><span class="name">King Prawns with Vegetables</span><span class="leader"></span><span class="price">$9.90</span></div>
      <div class="item"><span class="name">King Prawns with Black Bean Sauce</span><span class="leader"></span><span class="price">$9.90</span></div>
      <div class="item"><span class="name">Curried King Prawns with Vegetables</span><span class="leader"></span><span class="price">$9.90</span></div>
      <div class="item"><span class="name">King Prawn Cutlets (6)</span><span class="leader"></span><span class="price">$9.90</span></div>
      <div class="item"><span class="name">King Prawns with Cashew Nuts</span><span class="leader"></span><span class="price">$10.30</span></div>
      <div class="item"><span class="name">King Prawns with Almonds</span><span class="leader"></span><span class="price">$10.30</span></div>
      <div class="item"><span class="name">King Prawn Combination</span><span class="leader"></span><span class="price">$10.50</span></div>
      <div class="item"><span class="name">King Prawns with Ginger &amp; Shallot</span><span class="leader"></span><span class="price">$11.50</span></div>
      <div class="item"><span class="name">Garlic King Prawns</span><span class="leader"></span><span class="price">$11.50</span></div>
      <div class="item"><span class="name">Sate King Prawns</span><span class="leader"></span><span class="price">$11.50</span></div>
      <div class="item"><span class="name">King Prawns with Chilli Sauce</span><span class="leader"></span><span class="price">$11.50</span></div>
      <div class="item"><span class="name">Honey King Prawns</span><span class="leader"></span><span class="price">$11.50</span></div>
      <div class="item"><span class="name">King Prawn Fritters</span><span class="leader"></span><span class="price">$11.50</span></div>
      <div class="item"><span class="name">King Prawns with Szechuan Sauce (Hot)</span><span class="leader"></span><span class="price">$11.50</span></div>
      <div class="item"><span class="name">Crispy King Prawns with Salt and Pepper</span><span class="leader"></span><span class="price">$11.50</span></div>
      <div class="item"><span class="name">King Prawns with Garlic and Chilli Sauce</span><span class="leader"></span><span class="price">$11.50</span></div>
      <div class="item"><span class="name">King Prawns with Sweet Chilli Sauce</span><span class="leader"></span><span class="price">$11.50</span></div>
    </section>

    <section class="section" style="top:351px">
      <h2 class="section-title">Seafood</h2>
      <div class="item"><span class="name">Salt &amp; Pepper Squid</span><span class="leader"></span><span class="price">$10.00</span></div>
      <div class="item"><span class="name">Seafood Combination with Ginger &amp; Shallot</span><span class="leader"></span><span class="price">$12.00</span></div>
      <div class="item"><span class="name">Braised Scallops with Garlic Sauce</span><span class="leader"></span><span class="price">$12.00</span></div>
      <div class="item"><span class="name">Braised Scallops with Sate Sauce</span><span class="leader"></span><span class="price">$12.00</span></div>
      <div class="item"><span class="name">Braised Scallops with BBQ Sauce</span><span class="leader"></span><span class="price">$12.00</span></div>
      <div class="item"><span class="name">Braised Scallops with Mushrooms and Baby Corn</span><span class="leader"></span><span class="price">$12.00</span></div>
      <div class="item"><span class="name">Seafood Combination with Black Bean Sauce</span><span class="leader"></span><span class="price">$12.00</span></div>
      <div class="item"><span class="name">Seafood Combination with Oyster Sauce</span><span class="leader"></span><span class="price">$12.00</span></div>
      <div class="item"><span class="name">Seafood Combination with Sate Sauce</span><span class="leader"></span><span class="price">$12.00</span></div>
      <div class="item"><span class="name">Seafood Combination with Garlic and Chilli Sauce</span><span class="leader"></span><span class="price">$12.00</span></div>
    </section>

    <section class="section" style="top:566px">
      <h2 class="section-title">Beef</h2>
      <div class="item"><span class="name">Beef with Curry Sauce</span><span class="leader"></span><span class="price">$8.80</span></div>
      <div class="item"><span class="name">Beef with Black Bean Sauce</span><span class="leader"></span><span class="price">$8.80</span></div>
      <div class="item"><span class="name">Beef with Vegetables</span><span class="leader"></span><span class="price">$8.80</span></div>
      <div class="item"><span class="name">Beef with Almonds</span><span class="leader"></span><span class="price">$9.30</span></div>
      <div class="item"><span class="name">Beef with Cashew Nuts</span><span class="leader"></span><span class="price">$9.30</span></div>
      <div class="item"><span class="name">Beef with Ginger &amp; Shallot</span><span class="leader"></span><span class="price">$9.90</span></div>
      <div class="item"><span class="name">Beef with Oyster Sauce</span><span class="leader"></span><span class="price">$9.90</span></div>
      <div class="item"><span class="name">Beef with Garlic Sauce</span><span class="leader"></span><span class="price">$9.90</span></div>
      <div class="item"><span class="name">Beef with Garlic and Chilli Sauce</span><span class="leader"></span><span class="price">$9.90</span></div>
      <div class="item"><span class="name">Beef with Mongolian Sauce</span><span class="leader"></span><span class="price">$9.90</span></div>
      <div class="item"><span class="name">Beef with Black Pepper Sauce</span><span class="leader"></span><span class="price">$9.90</span></div>
      <div class="item"><span class="name">Beef with Sate Sauce</span><span class="leader"></span><span class="price">$9.90</span></div>
      <div class="item"><span class="name">Beef with Chilli Sauce</span><span class="leader"></span><span class="price">$9.90</span></div>
      <div class="item"><span class="name">Beef with Barbecue Sauce</span><span class="leader"></span><span class="price">$9.90</span></div>
      <div class="item"><span class="name">Beef with Szechaun Sauce (Hot)</span><span class="leader"></span><span class="price">$9.90</span></div>
    </section>
  </div>

  <div class="column column--right">
    <section class="section" style="top:8px">
      <h2 class="section-title">Lamb</h2>
      <div class="item"><span class="name">Mongolian Lamb Fillet</span><span class="leader"></span><span class="price">$10.80</span></div>
      <div class="item"><span class="name">Lamb with BBQ Sauce</span><span class="leader"></span><span class="price">$10.80</span></div>
      <div class="item"><span class="name">Lamb with Szechuan Sauce (Hot)</span><span class="leader"></span><span class="price">$10.80</span></div>
      <div class="item"><span class="name">Lamb with Garlic and Chilli Sauce</span><span class="leader"></span><span class="price">$10.80</span></div>
      <div class="item"><span class="name">Lamb with Sate Sauce</span><span class="leader"></span><span class="price">$10.80</span></div>
      <div class="item"><span class="name">Lamb with Garlic Sauce</span><span class="leader"></span><span class="price">$10.80</span></div>
      <div class="item"><span class="name">Lamb with Black Pepper Sauce</span><span class="leader"></span><span class="price">$10.80</span></div>
      <div class="item"><span class="name">Deep Fried Lamb Fillet with Special Sauce</span><span class="leader"></span><span class="price">$10.80</span></div>
    </section>

    <section class="section" style="top:168px">
      <h2 class="section-title">Chicken</h2>
      <div class="item" style="line-height:17.2px"><span class="name">Braised Chicken with Curry Sauce</span><span class="leader"></span><span class="price">$8.80</span></div>
      <div class="item" style="line-height:17.2px"><span class="name">Braised Chicken with Vegetables</span><span class="leader"></span><span class="price">$8.80</span></div>
      <div class="item" style="line-height:17.2px"><span class="name">Braised Chicken with Black Bean Sauce</span><span class="leader"></span><span class="price">$8.80</span></div>
      <div class="item" style="line-height:17.2px"><span class="name">Braised Chicken with Cashew Nuts</span><span class="leader"></span><span class="price">$9.30</span></div>
      <div class="item" style="line-height:17.2px"><span class="name">Braised Chicken with Almonds</span><span class="leader"></span><span class="price">$9.30</span></div>
      <div class="item" style="line-height:17.2px"><span class="name">Garlic Butter Chicken</span><span class="leader"></span><span class="price">$9.90</span></div>
      <div class="item" style="line-height:17.2px"><span class="name">Braised Chicken with Ginger &amp; Shallot</span><span class="leader"></span><span class="price">$9.90</span></div>
      <div class="item" style="line-height:17.2px"><span class="name">Braised Chicken with Sate Sauce</span><span class="leader"></span><span class="price">$9.90</span></div>
      <div class="item" style="line-height:17.2px"><span class="name">Lemon Chicken Fritters</span><span class="leader"></span><span class="price">$9.90</span></div>
      <div class="item" style="line-height:17.2px"><span class="name">Honey Chicken Fritters</span><span class="leader"></span><span class="price">$9.90</span></div>
      <div class="item" style="line-height:17.2px"><span class="name">Braised Chicken in Garlic Sauce</span><span class="leader"></span><span class="price">$9.90</span></div>
      <div class="item" style="line-height:17.2px"><span class="name">Braised Chicken with Chilli Sauce</span><span class="leader"></span><span class="price">$9.90</span></div>
      <div class="item" style="line-height:17.2px"><span class="name">Braised Chicken with Garlic and Chilli Sauce</span><span class="leader"></span><span class="price">$9.90</span></div>
      <div class="item" style="line-height:17.2px"><span class="name">Braised Chicken with Sweet Chilli Sauce</span><span class="leader"></span><span class="price">$9.90</span></div>
      <div class="item" style="line-height:17.2px"><span class="name">Braised Chicken with Szechaun Sauce (Hot)</span><span class="leader"></span><span class="price">$9.90</span></div>
    </section>

    <section class="section" style="top:456px">
      <h2 class="section-title">Pork</h2>
      <div class="item"><span class="name">Pork with Black Bean Sauce</span><span class="leader"></span><span class="price">$8.80</span></div>
      <div class="item"><span class="name">Pork with Vegetables</span><span class="leader"></span><span class="price">$8.80</span></div>
      <div class="item"><span class="name">Pork with Almonds</span><span class="leader"></span><span class="price">$9.30</span></div>
      <div class="item"><span class="name">Pork with Cashew Nuts</span><span class="leader"></span><span class="price">$9.30</span></div>
      <div class="item"><span class="name">Pork with Ginger &amp; Shallot</span><span class="leader"></span><span class="price">$9.90</span></div>
      <div class="item"><span class="name">Pork with Szechuan Sauce (Hot)</span><span class="leader"></span><span class="price">$9.90</span></div>
      <div class="item"><span class="name">Pork with BBQ Sauce</span><span class="leader"></span><span class="price">$9.90</span></div>
      <div class="item"><span class="name">Pork with Garlic Sauce</span><span class="leader"></span><span class="price">$9.90</span></div>
      <div class="item"><span class="name">Pork with Chilli Sauce</span><span class="leader"></span><span class="price">$9.90</span></div>
      <div class="item"><span class="name">Pork with Sate Sauce</span><span class="leader"></span><span class="price">$9.90</span></div>
      <div class="item"><span class="name">Pork with Mongolian Sauce</span><span class="leader"></span><span class="price">$9.90</span></div>
      <div class="item"><span class="name">Pork with Sweet Chilli Sauce</span><span class="leader"></span><span class="price">$9.90</span></div>
      <div class="item"><span class="name">BBQ Pork with Plum Sauce</span><span class="leader"></span><span class="price">$9.90</span></div>
      <div class="item"><span class="name">BBQ Pork with Black Bean Sauce</span><span class="leader"></span><span class="price">$9.90</span></div>
      <div class="item"><span class="name">Salt &amp; Pepper Pork</span><span class="leader"></span><span class="price">$10.00</span></div>
    </section>

    <section class="section" style="top:734px">
      <h2 class="section-title">Vegetables</h2>
      <div class="item"><span class="name">Stir-Fried Mixed Vegetables</span><span class="leader"></span><span class="price">$7.00</span></div>
      <div class="item"><span class="name">Steamed Mixed Vegetables with Oyster Sauce</span><span class="leader"></span><span class="price">$7.00</span></div>
      <div class="item"><span class="name">Mixed Vegetables with Curry Sauce</span><span class="leader"></span><span class="price">$7.00</span></div>
      <div class="item"><span class="name">Mixed Vegetables with Black Bean Sauce</span><span class="leader"></span><span class="price">$7.00</span></div>
      <div class="item"><span class="name">Mixed Vegetables with Baby Corn &amp; Mushrooms</span><span class="leader"></span><span class="price">$8.00</span></div>
      <div class="item"><span class="name">Broccoli with Crabmeat Sauce</span><span class="leader"></span><span class="price">$8.80</span></div>
    </section>
  </div>

  <div class="footer-rule"></div>
  <p class="footer">All dishes served with: Fried Rice • Boiled Rice • Soft Noodles or Thick Rice Noodles $1.50 extra</p>
</div>
</body>
</html>
```